Moravel Stenwick Inc needs a business card design

Looking for a unique, classy and sharp business card design.

Contact Information for Business Card

Moravel Stenwick Inc.
Marisa Ortega Bellido BScOT(c)
Occupational Therapist
(780) 555-0142
moravelstenwick@postlynx.net

```html
<!DOCTYPE html>
<html lang="en">
<head>
<meta charset="utf-8">
<title>Moravel Stenwick Inc. – Business Card</title>
<link rel="stylesheet" href="https://fonts.googleapis.com/css2?family=Khand:wght@400;500&family=Saira+Condensed:wght@600&display=swap">
<style>
  :root {
    --backdrop: #ece8e4;
    --card: #ffffff;
    --purple: #8a1f8c;
    --green: #8cc63f;
    --soft-green: #eef6e4;
    --soft-blue: #e3f1f9;
    --ink: #3f3f3f;
  }
  * { margin: 0; padding: 0; box-sizing: border-box; }
  html, body {
    width: 1200px; height: 1200px; overflow: hidden;
    background: var(--backdrop);
  }
  .canvas {
    position: relative; width: 1200px; height: 1200px;
  }
  .card {
    position: absolute; left: 315px; top: 101px;
    width: 570px; height: 998px;
    background: var(--card);
    border-radius: 285px 285px 4px 4px;
    box-shadow: 0 6px 18px rgba(0,0,0,.18);
    overflow: hidden;
    text-align: center;
  }
  .brand {
    position: absolute; top: 225px; left: 0; right: 0;
    display: flex; align-items: center; justify-content: center; gap: 14px;
    font-family: "Saira Condensed", sans-serif; font-weight: 600;
    font-size: 50px; color: var(--purple); line-height: 1;
  }
  .brand-dot {
    width: 26px; height: 26px; border-radius: 50%; background: var(--green);
  }
  .backdrop-mark {
    position: absolute; left: 70px; top: 760px;
    width: 450px; height: 300px; border-radius: 50% 50% 0 0;
    background: radial-gradient(ellipse at 50% 45%, var(--soft-blue) 0%, var(--soft-green) 45%, rgba(255,255,255,0) 72%);
  }
  .holder {
    position: absolute; top: 612px; left: 0; right: 0;
  }
  .holder-name {
    font-family: "Saira Condensed", sans-serif; font-weight: 600;
    font-size: 34px; color: var(--purple); line-height: 1.1; letter-spacing: .3px;
  }
  .holder-role {
    font-family: "Khand", sans-serif; font-weight: 400;
    font-size: 27px; color: var(--ink); line-height: 1.2; letter-spacing: .5px;
  }
  .divider {
    position: absolute; top: 716px; left: 241px;
    width: 88px; height: 3px; background: var(--green);
  }
  .contact {
    position: absolute; top: 740px; left: 0; right: 0;
    font-family: "Khand", sans-serif; color: var(--ink);
  }
  .company {
    font-family: "Saira Condensed", sans-serif; font-weight: 600;
    font-size: 23px; color: var(--purple); margin-bottom: 12px;
  }
  .contact-line {
    display: flex; align-items: center; justify-content: center; gap: 10px;
    font-size: 25px; line-height: 35px; letter-spacing: .3px;
  }
  .contact-line svg { fill: var(--purple); }
</style>
</head>
<body>
<div class="canvas">
  <div class="card">
    <div class="brand">
      <span class="brand-dot"></span>
      <span class="brand-name">Moravel Stenwick</span>
    </div>

    <div class="backdrop-mark" role="img" aria-label="Faint brand decoration in soft green and blue"></div>

    <div class="holder">
      <p class="holder-name">Marisa Ortega Bellido BScOT(c)</p>
      <p class="holder-role">Occupational Therapist</p>
    </div>

    <div class="divider"></div>

    <div class="contact">
      <p class="company">Moravel Stenwick Inc.</p>
      <p class="contact-line">
        <svg width="20" height="20" viewBox="0 0 24 24" aria-hidden="true"><path d="M6.6 10.8a15.1 15.1 0 0 0 6.6 6.6l2.2-2.2c.3-.3.7-.4 1-.2 1.1.4 2.3.6 3.6.6.6 0 1 .4 1 1V20c0 .6-.4 1-1 1A17 17 0 0 1 3 4c0-.6.4-1 1-1h3.5c.6 0 1 .4 1 1 0 1.3.2 2.5.6 3.6.1.3 0 .7-.2 1z"/></svg>
        <span>(780) 555-0142</span>
      </p>
      <p class="contact-line">
        <svg width="26" height="18" viewBox="0 0 26 18" aria-hidden="true"><path d="M0 0h26v18H0z M2 2v.6l11 7.4 11-7.4V2z M2 5v11h22V5l-11 7.4z" fill-rule="evenodd"/></svg>
        <span>moravelstenwick@postlynx.net</span>
      </p>
    </div>
  </div>
</div>
</body>
</html>
```